Edit current business card design

Need business card design where Business Name, Logo, Address, phone and fax, website address are permanent.Need to be able to add and edit employee name and email address.

Business

```html
<!DOCTYPE html>
<html lang="en">
<head>
<meta charset="utf-8">
<title>Morrow's Accounting Services – Business Cards</title>
<link href="https://fonts.googleapis.com/css2?family=Open+Sans:wght@400;600&display=swap" rel="stylesheet">
<style>
  :root {
    --backdrop: #3a332f;
    --card-black: #1b1c1c;
    --card-black-edge: #2a2b2b;
    --brand-green: #2f6e48;
    --brand-green-light: #3f8a5c;
    --card-green: #2e5d3f;
    --text-light: #e9ece9;
    --text-muted: #c9cfca;
    --divider: #3c3e3d;
  }
  * { box-sizing: border-box; margin: 0; padding: 0; }
  html, body {
    width: 1200px; height: 844px; overflow: hidden;
    background: var(--backdrop);
    font-family: "Open Sans", Arial, sans-serif;
  }
  .stage {
    position: relative; width: 1200px; height: 844px;
    display: flex; align-items: center; justify-content: center; gap: 60px;
  }
  .card {
    width: 520px; height: 297px; position: relative; border-radius: 3px;
    box-shadow: 0 14px 30px rgba(0,0,0,.45);
  }
  /* Front */
  .card-front {
    background: linear-gradient(135deg, var(--card-black) 0%, var(--card-black-edge) 100%);
    display: flex;
  }
  .brand {
    width: 270px; display: flex; flex-direction: column;
    align-items: center; justify-content: center; gap: 10px;
    border-right: 1px solid var(--divider);
    margin: 40px 0;
  }
  .brand-dot {
    width: 64px; height: 64px; border-radius: 50%;
    background: var(--brand-green);
  }
  .brand-name {
    color: var(--brand-green-light); font-weight: 600;
    text-align: center; line-height: 1.15;
  }
  .brand-name .main { display: block; font-size: 30px; letter-spacing: 2px; text-transform: uppercase; }
  .brand-name .sub { display: block; font-size: 14px; letter-spacing: 1.5px; }
  .contact {
    flex: 1; padding: 58px 0 0 24px; color: var(--text-light); font-size: 13px; line-height: 1.4;
  }
  .contact-name { color: var(--brand-green-light); font-size: 15px; font-weight: 600; }
  .contact-title { margin-bottom: 14px; }
  .contact-address { margin-bottom: 14px; }
  .contact-line { display: flex; align-items: center; gap: 8px; }
  .contact-line svg { width: 11px; height: 11px; fill: var(--brand-green-light); flex: none; }
  /* Back */
  .card-back {
    background: var(--card-green);
    color: var(--text-light); text-align: center;
    padding-top: 38px; font-size: 13.5px; line-height: 1.45;
  }
  .services-title { text-decoration: underline; margin-bottom: 6px; font-size: 14px; }
  .services-list { list-style: none; }
  .tagline { margin-top: 40px; font-size: 14px; }
</style>
</head>
<body>
<main class="stage">
  <section class="card card-front" aria-label="Business card front">
    <div class="brand">
      <span class="brand-dot" aria-hidden="true"></span>
      <p class="brand-name"><span class="main">Morrow's</span><span class="sub">Accounting Services</span></p>
    </div>
    <div class="contact">
      <p class="contact-name">Dale Morrow</p>
      <p class="contact-title">EA,ATA,ATP</p>
      <p class="contact-address">12345, Address Goes Here<br>Country Name, 123456.</p>
      <p class="contact-line">
        <svg viewBox="0 0 24 24" aria-hidden="true"><path d="M6.6 10.8a15 15 0 0 0 6.6 6.6l2.2-2.2a1 1 0 0 1 1-.25 11.4 11.4 0 0 0 3.6.57 1 1 0 0 1 1 1V20a1 1 0 0 1-1 1A17 17 0 0 1 3 4a1 1 0 0 1 1-1h3.5a1 1 0 0 1 1 1c0 1.25.2 2.45.57 3.57a1 1 0 0 1-.25 1z"/></svg>
        044-123 456 789</p>
      <p class="contact-line">
        <svg viewBox="0 0 24 24" aria-hidden="true"><path d="M2 5h20v14H2z M2 5l10 8 10-8" /></svg>
        info@morrowledger.com</p>
      <p class="contact-line">
        <svg viewBox="0 0 24 24" aria-hidden="true"><path d="M10 14a4 4 0 0 1 0-5.6l3-3a4 4 0 0 1 5.6 5.6l-1.5 1.5-1.4-1.4 1.5-1.5a2 2 0 0 0-2.8-2.8l-3 3a2 2 0 0 0 0 2.8zm4-4a4 4 0 0 1 0 5.6l-3 3a4 4 0 0 1-5.6-5.6l1.5-1.5 1.4 1.4-1.5 1.5a2 2 0 0 0 2.8 2.8l3-3a2 2 0 0 0 0-2.8z"/></svg>
        www.morrowledger.com</p>
    </div>
  </section>

  <section class="card card-back" aria-label="Business card back">
    <h2 class="services-title" style="font-weight:400">SERVICES</h2>
    <ul class="services-list">
      <li>Tax planning &amp; preparation for business &amp; individuals</li>
      <li>Tax problem resolutions</li>
      <li>Bookkeeping and Payroll Services</li>
      <li>Incorporation &amp; new business advisor</li>
      <li>Bookkeeping support &amp; training</li>
      <li>And more….</li>
    </ul>
    <p class="tagline">Helping our Clients Keep More of What They Make</p>
  </section>
</main>
</body>
</html>
```